Plorvan Pte Ltd

I want a creative and stand out web page so when my client search for my web page or google search. The front page is stand out and they know that we are the interior office designer that are searching for . We are commercial office design company. We also have the video to put at our front page for client to see. Natural is the key elements. As we like to carry recycle materials , plant , trees is our key element such as biophilic design
Updates

Hi All,

For my web page, I need minimalist design and creative frontpage.
When my client search for my web page, they straight feel that this is the office design company.
The webpage is special and nature is the key element for the design.
My company logo can be design in the shaped of the letter OO in the webpage.
Below is the sample you can refer.

https://www.mavrelink.example/pin/271950364812057329/

Target Market(s)

Customer searching for office design

Industry/Entity Type

Commerical designer firm- Office interior design & Build company

Number of Pages Required

5+ page

Font styles to use
Other font styles liked:
• Wilmina

Colors
59FF00
82FF00
B8FF75
E3FFCB
F4FFEA
FFC000
F8CF3A
FAE287
FDF2CF
FEFAEE
6B429C
8869AF
B7A5CE
E3DAEB
F3F0F8

Requirements
Must have
• Home, Services,Gallery, Calculator, Testimonials, Contact, Blog
Nice to have
• Natural, creative, minimalist
Should not have
• No black color or blue color

```html
<!DOCTYPE html>
<html lang="en">
<head>
<meta charset="utf-8">
<title>Plorvan Pte Ltd — Office Interior Design</title>
<link rel="stylesheet" href="https://fonts.googleapis.com/css2?family=Outfit:wght@500;600;700&family=Roboto:ital,wght@0,400;0,500;1,400&display=swap">
<style>
:root{
  --yellow:#FFC000;
  --yellow-soft:#F8CF3A;
  --ink:#222222;
  --text:#444444;
  --line:#e2e2e2;
  --panel:#f1f1f1;
  --white:#ffffff;
  --footer:#242424;
}
*{box-sizing:border-box;margin:0;padding:0}
html,body{width:1200px;height:4934px;overflow:hidden}
body{position:relative;background:var(--white);font-family:'Roboto',sans-serif;color:var(--text)}
.abs{position:absolute}
h1,h2,h3{font-family:'Outfit',sans-serif;color:var(--ink);font-weight:600}
.btn{display:inline-flex;align-items:center;gap:8px;background:var(--yellow);color:var(--ink);font:500 13px 'Roboto',sans-serif;text-decoration:underline;padding:0 22px;height:44px}
.btn svg{width:14px;height:14px}

/* nav */
.site-nav{top:0;left:0;width:1200px;height:76px}
.brand{left:150px;top:26px;display:flex;align-items:center;gap:8px;font:600 16px 'Outfit',sans-serif;color:var(--ink)}
.brand-mark{width:12px;height:12px;background:var(--yellow)}
.menu{right:150px;top:30px;display:flex;gap:28px;font:500 13px 'Roboto',sans-serif;color:var(--ink)}

/* hero */
.hero{top:76px;left:0;width:1200px;height:480px;background:linear-gradient(180deg,#ffffff 0%,#f4f4f4 100%)}
.hero-sketch{left:150px;top:0;width:420px;height:400px;background:linear-gradient(160deg,rgba(236,236,236,.45),rgba(248,248,248,0) 70%)}
.hero-title{left:150px;top:44px;font-size:54px;line-height:60px;font-weight:700;width:420px}
.hero .btn{left:150px;top:244px;height:40px}
.hero-video{left:606px;top:54px;width:368px;height:232px;background:linear-gradient(135deg,#3a3a3a,#111 60%,#2c2a25)}
.play{left:170px;top:102px;width:30px;height:30px;border-radius:50%;background:var(--yellow);border:3px solid #fff}
.play::after{content:"";position:absolute;left:9px;top:6px;border-left:10px solid #fff;border-top:6px solid transparent;border-bottom:6px solid transparent}
.hero-tiles{left:999px;top:54px;display:flex;flex-direction:column;gap:18px}
.tile{width:51px;height:51px;display:flex;align-items:center;justify-content:center}
.tile.dark{background:#1e1e1e}
.tile.gold{background:var(--yellow)}
.tile.light{background:#fff;box-shadow:0 2px 8px rgba(0,0,0,.1)}
.hero-intro{left:606px;top:304px;width:444px;border-left:4px solid var(--yellow);padding-left:18px;font:italic 13px/27px 'Roboto',sans-serif;color:var(--ink)}

/* welcome */
.welcome{top:556px;left:0;width:1200px;height:575px}
.welcome-forest{inset:0;background:linear-gradient(180deg,#f1f1f1 0%,#e4e7e3 45%,#9aa79a 75%,#3c5a43 100%)}
.welcome h2{top:116px;left:0;width:1200px;text-align:center;font-size:38px}
.welcome p{top:178px;left:160px;width:880px;text-align:center;font-size:13px;line-height:27px;color:var(--ink)}

/* choice */
.choice{top:1221px;left:0;width:1200px;height:395px}
.choice-band{left:0;top:0;width:291px;height:395px;background:var(--yellow-soft)}
.choice-photo{left:151px;top:37px;width:363px;height:322px;background:linear-gradient(160deg,#6f5a2a,#2d2a14 55%,#8d7a3a)}
.choice h2{left:606px;top:34px;font-size:38px;line-height:46px;width:400px}
.choice p{left:606px;top:148px;width:444px;font-size:13px;line-height:27px}
.choice .btn{left:606px;top:314px}

/* calculators */
.calc-title{top:1705px;left:0;width:1200px;text-align:center;font-size:38px}
.calc-row{top:1796px;left:150px;display:flex;gap:12px}
.calc-card{position:relative;width:292px;height:343px;background:#fff;box-shadow:0 3px 14px rgba(0,0,0,.08);text-align:center;padding-top:108px}
.calc-icon{position:absolute;left:96px;top:0;width:100px;height:100px;border-radius:50%;background:var(--yellow);border:5px solid #fff;box-shadow:0 2px 8px rgba(0,0,0,.12);display:flex;align-items:center;justify-content:center}
.calc-card h3{font-size:23px;line-height:30px;margin-bottom:18px}
.calc-card p{font-size:12.5px;line-height:27px;padding:0 36px}

/* gallery */
.gallery{top:2249px;left:0;width:1200px;height:770px;background:var(--panel)}
.gallery h2{top:76px;left:0;width:1200px;text-align:center;font-size:38px}
.gallery-sub{top:144px;left:0;width:1200px;text-align:center;font-size:13px}
.tabs{top:192px;left:150px;width:898px;display:flex;justify-content:space-between;font:500 12.5px 'Roboto',sans-serif;color:var(--ink)}
.tabs .active{color:var(--yellow);border-bottom:2px solid var(--yellow);padding-bottom:4px}
.grid{top:236px;left:150px;display:grid;grid-template-columns:292px 292px 292px;grid-auto-rows:220px;gap:21px 11px}
.shot{background:linear-gradient(160deg,#d9d4cb,#8d8273 60%,#c9c3b9)}
.shot.b{background:linear-gradient(160deg,#ece7de,#b49a6d 60%,#7b776f)}
.shot.c{background:linear-gradient(160deg,#f3efe8,#a19788 55%,#5f4c3b)}
.shot.d{background:linear-gradient(160deg,#dcd8d2,#6e5244 60%,#9d9893)}
.shot.e{background:linear-gradient(160deg,#eef0f2,#c5c5c5 50%,#6c6670)}
.shot.f{background:linear-gradient(160deg,#d7c79a,#7f8f3a 50%,#354a6a)}
.gallery-trees{left:0;bottom:0;width:1200px;height:80px;background:linear-gradient(180deg,rgba(241,241,241,0),#d9d9d9)}

/* newsletter */
.news h2{top:3108px;left:150px;font-size:38px;line-height:46px}
.news p{top:3220px;left:152px;font-size:12.5px;line-height:27px;color:var(--ink)}
.news-input{top:3169px;left:529px;width:520px;height:38px;border:1px solid #ccc;border-radius:3px;padding-left:24px;font:12px/36px 'Roboto',sans-serif;color:#aaa}
.news .btn{top:3222px;left:529px;width:520px;height:39px;justify-content:center}

/* services */
.services h2{top:3376px;left:0;width:1200px;text-align:center;font-size:38px;line-height:46px}
.services p{top:3476px;left:160px;width:880px;text-align:center;font-size:13px;line-height:27px;color:var(--ink)}
.svc-row{top:3604px;left:150px;display:flex;gap:11px}
.svc-card{width:217px;height:216px;background:#fff;box-shadow:0 3px 14px rgba(0,0,0,.08);text-align:center;padding-top:30px}
.svc-icon{width:86px;height:86px;margin:0 auto 10px;border-radius:50%;background:var(--yellow);border:4px solid #fff;box-shadow:0 2px 8px rgba(0,0,0,.12);display:flex;align-items:center;justify-content:center}
.svc-card h3{font-size:23px;line-height:30px;font-weight:500}

/* contact */
.touch{top:3935px;left:606px;font-size:38px}
.contact-h{top:4022px;left:150px;font-size:38px}
.info{left:150px;display:flex;gap:14px;font-size:13px;line-height:26px;color:var(--ink)}
.info svg{flex:none;margin-top:4px}
.field{left:606px;width:443px;border-bottom:1.5px solid var(--yellow-soft);font-size:10px;color:var(--ink)}
.contact-form .btn{left:606px;top:4354px;height:46px}

/* footer */
.footer-trees{top:4486px;left:0;width:1200px;height:106px;background:linear-gradient(180deg,rgba(255,255,255,0),var(--footer))}
.footer{top:4591px;left:0;width:1200px;height:343px;background:var(--footer);color:#ddd}
.f-brand{left:150px;top:64px;display:flex;align-items:center;gap:10px;font:600 24px 'Outfit',sans-serif;color:#eeeeee}
.f-brand .brand-mark{width:16px;height:16px}
.f-badge{left:278px;top:106px;width:46px;height:24px;border-radius:4px;background:#555}
.follow{left:150px;top:161px;font-size:12px}
.socials{left:150px;top:197px;display:flex;gap:13px}
.socials span{width:29px;height:29px;border-radius:50%;background:var(--yellow)}
.f-col h3{color:#fff;font-size:20px;font-weight:500;margin-bottom:18px}
.f-links li{list-style:none;font-size:12.5px;line-height:31.5px}
.f-info{display:flex;gap:12px;font-size:11.5px;line-height:24px;margin-bottom:16px}
.copy-line{top:294px;left:0;width:1200px;border-top:1px solid #444}
.copy{top:314px;left:0;width:1200px;text-align:center;font-size:11px;color:#bbb}
</style>
</head>
<body>

<header class="site-nav abs">
  <div class="brand abs"><span class="brand-mark"></span>Plorvan Pte Ltd</div>
  <nav class="menu abs"><span>About</span><span>Services</span><span>Gallery</span><span>Calculators</span><span>Blog</span><span>Contact</span></nav>
</header>

<section class="hero abs">
  <div class="hero-sketch abs" role="img" aria-label="Line sketch of a modern building interior"></div>
  <h1 class="hero-title abs">Transforming Spaces with Expertise</h1>
  <a class="btn abs">Explore Our Project Gallery <svg viewBox="0 0 14 14"><path d="M1 7h11M8 3l4 4-4 4" fill="none" stroke="#222" stroke-width="1.6"/></svg></a>
  <div class="hero-video abs" role="img" aria-label="Video still of a dark office corridor with display walls">
    <span class="play abs"></span>
  </div>
  <div class="hero-tiles abs">
    <div class="tile dark"><svg width="24" height="24" viewBox="0 0 24 24"><path d="M5 19L19 5M9 5h10v10" fill="none" stroke="#FFC000" stroke-width="2"/></svg></div>
    <div class="tile gold"><svg width="26" height="26" viewBox="0 0 26 26"><path d="M4 22L22 4M4 4l18 18" stroke="#fff" stroke-width="2"/></svg></div>
    <div class="tile light"><svg width="26" height="26" viewBox="0 0 26 26"><rect x="4" y="4" width="18" height="18" fill="none" stroke="#FFC000" stroke-width="2"/><path d="M8 18l10-10" stroke="#FFC000" stroke-width="2"/></svg></div>
  </div>
  <p class="hero-intro abs">Plorvan is an interior design and renovation company that specialises in office interior design and commercial retail renovation. We always aim to provide premium quality services with competitive cost and ensuring our clients are pleased with the outcome.</p>
</section>

<section class="welcome abs">
  <div class="welcome-forest abs" role="img" aria-label="Misty pine forest"></div>
  <h2 class="abs">Welcome to Plorvan singapore</h2>
  <p class="abs">No matter what type of commercial space you have, whether it is an office, corporate firm, restaurant, spa, salon, plaza, mall, or any retail shop, we are here to provide the highest level of interior design and renovation services to match your needs. Our creative ideas and innovative solutions to commercial renovation projects can transform any workspace or building into a masterpiece. Let our professional and experienced team of designers turn your dreams into reality – one step at a time.</p>
</section>

<section class="choice abs">
  <div class="choice-band abs"></div>
  <div class="choice-photo abs" role="img" aria-label="Sunlit forest path between tall trees"></div>
  <h2 class="abs">What makes us the right choice?</h2>
  <p class="abs">The secret to our exemplary work lies in the kind of professionals that we choose to bring into our team. We have assembled a team of interior designers who are always looking to face fresh challenges set before them. As a matter of fact, we like to encourage competition among our designers.</p>
  <a class="btn abs">Know more <svg viewBox="0 0 14 14"><path d="M1 7h11M8 3l4 4-4 4" fill="none" stroke="#222" stroke-width="1.6"/></svg></a>
</section>

<h2 class="calc-title abs">Our calculators</h2>
<div class="calc-row abs">
  <article class="calc-card">
    <div class="calc-icon"><svg width="50" height="50" viewBox="0 0 50 50" fill="none" stroke="#222" stroke-width="2"><rect x="14" y="8" width="24" height="16"/><path d="M8 30h34M12 30v14M38 30v14M18 38h8"/></svg></div>
    <h3>Office Floor<br>Space Calculator</h3>
    <p>Unsure how much office space do you need for renovation? Use our office space calculator here.</p>
  </article>
  <article class="calc-card">
    <div class="calc-icon"><svg width="50" height="50" viewBox="0 0 50 50" fill="none" stroke="#222" stroke-width="2"><circle cx="25" cy="22" r="12"/><path d="M25 14v16M21 18h6a2 2 0 010 4h-4a2 2 0 000 4h6M10 40l8-6"/></svg></div>
    <h3>Renovation Budget<br>Calculator</h3>
    <p>How much should you budget for office renovation? Try out our renovation budget calculator here.</p>
  </article>
  <article class="calc-card">
    <div class="calc-icon"><svg width="50" height="50" viewBox="0 0 50 50" fill="none" stroke="#222" stroke-width="2"><rect x="8" y="8" width="10" height="8"/><rect x="8" y="22" width="10" height="8"/><rect x="8" y="36" width="10" height="8"/><rect x="32" y="15" width="10" height="8"/><rect x="32" y="30" width="10" height="8"/><path d="M18 12h8v22h6M26 19h6M18 26h8"/></svg></div>
    <h3>Project Timeline<br>Calculator</h3>
    <p>In order to know your office renovation and relocation timescale. Use this project timeline calculator.</p>
  </article>
</div>

<section class="gallery abs">
  <h2 class="abs">Project gallery</h2>
  <p class="gallery-sub abs">Explore our work. Let our design portfolio speaks for itself.</p>
  <div class="tabs abs"><span class="active">All</span><span>Tarnell Freight Singapore</span><span>KVRAE</span><span>Merandi Utama Holdings</span><span>Farwind Hotels</span><span>Tarnell Freight Kuala Lumpur</span><span>Lumeros Singapore</span></div>
  <div class="grid abs">
    <div class="shot" role="img" aria-label="Open office with curved windows and lounge seating"></div>
    <div class="shot b" role="img" aria-label="Timber staircase and reception area"></div>
    <div class="shot c" role="img" aria-label="Boardroom with long white table"></div>
    <div class="shot d" role="img" aria-label="Meeting room with dark chairs and window blinds"></div>
    <div class="shot e" role="img" aria-label="Reception counter with patterned carpet"></div>
    <div class="shot f" role="img" aria-label="Breakout lounge with green sofa"></div>
  </div>
  <div class="gallery-trees abs" role="img" aria-label="Faint tree line along the bottom edge"></div>
</section>

<section class="news">
  <h2 class="abs">Subscribe our<br>newsletter</h2>
  <p class="abs">Magna in elementum vulputate vulputate sed.<br>Pulvinar posuere turpis eget in semper. Id.</p>
  <div class="news-input abs">Example123@email.com</div>
  <a class="btn abs">Subscribe <svg viewBox="0 0 14 14"><path d="M1 7h11M8 3l4 4-4 4" fill="none" stroke="#222" stroke-width="1.6"/></svg></a>
</section>

<section class="services">
  <h2 class="abs">Your one-stop office renovation &amp;<br>interior design partner</h2>
  <p class="abs">Designing a new office or remolding an existing one involves a tedious process. Plorvan wants to make it easier for you. We will guide you from start to end of the journey. To ensure that the project will be well organised and communicated, a dedicated project manager will be assigned. Discover our various services that can turn your creative ideas into reality.</p>
  <div class="svc-row abs">
    <article class="svc-card"><div class="svc-icon"><svg width="40" height="40" viewBox="0 0 40 40" fill="none" stroke="#222" stroke-width="2"><path d="M6 34L34 6M6 6l10 10M24 24l10 10"/><rect x="6" y="26" width="8" height="8"/></svg></div><h3>Office interior<br>design</h3></article>
    <article class="svc-card"><div class="svc-icon"><svg width="40" height="40" viewBox="0 0 40 40" fill="none" stroke="#222" stroke-width="2"><path d="M6 18L20 6l14 12M10 16v18h20V16"/><rect x="17" y="24" width="6" height="10"/></svg></div><h3>Office<br>renovation</h3></article>
    <article class="svc-card"><div class="svc-icon"><svg width="40" height="40" viewBox="0 0 40 40" fill="none" stroke="#222" stroke-width="2"><rect x="5" y="8" width="30" height="24"/><path d="M5 18h30M15 8v24M25 8v24"/></svg></div><h3>Office space<br>planning</h3></article>
    <article class="svc-card"><div class="svc-icon"><svg width="40" height="40" viewBox="0 0 40 40" fill="none" stroke="#222" stroke-width="2"><path d="M8 34V10M20 34V6M32 34V10M4 34h32"/><circle cx="26" cy="14" r="3"/></svg></div><h3>Office space<br>partitioning</h3></article>
  </div>
</section>

<section class="contact">
  <h2 class="touch abs">Get in touch with us</h2>
  <h2 class="contact-h abs">Contact us</h2>
  <div class="info abs" style="top:4094px"><svg width="16" height="18" viewBox="0 0 16 18"><path d="M8 17s6-6 6-10A6 6 0 002 7c0 4 6 10 6 10z" fill="#FFC000"/><circle cx="8" cy="7" r="2" fill="#fff"/></svg><span>14 Orvale Lane #05-11/11A Brenholt<br>House Singapore 000214</span></div>
  <div class="info abs" style="top:4162px"><svg width="16" height="16" viewBox="0 0 16 16"><path d="M3 1l3 3-2 2c1 2 3 4 5 5l2-2 3 3-2 3C7 15 1 9 1 3z" fill="#FFC000"/></svg><span>+65 6000 1280</span></div>
  <div class="info abs" style="top:4210px"><svg width="16" height="18" viewBox="0 0 16 18"><rect x="3" y="1" width="10" height="16" rx="1.5" fill="none" stroke="#FFC000" stroke-width="2"/></svg><span>+65 9000 4617</span></div>
  <div class="info abs" style="top:4258px"><svg width="16" height="14" viewBox="0 0 16 14"><rect x="1" y="2" width="14" height="10" fill="#FFC000"/><path d="M1 2l7 5 7-5" fill="none" stroke="#fff" stroke-width="1.2"/></svg><span>hello@plorvan.example</span></div>

  <form class="contact-form">
    <div class="field abs" style="top:4006px;height:48px">Name*</div>
    <div class="field abs" style="top:4081px;height:50px">Phone number*</div>
    <div class="field abs" style="top:4157px;height:50px">Email address*</div>
    <div class="field abs" style="top:4232px;height:100px">Message</div>
    <a class="btn abs">Submit <svg viewBox="0 0 14 14"><path d="M1 7h11M8 3l4 4-4 4" fill="none" stroke="#222" stroke-width="1.6"/></svg></a>
  </form>
</section>

<div class="footer-trees abs" role="img" aria-label="Dark pine tree silhouette line"></div>
<footer class="footer abs">
  <div class="f-brand abs"><span class="brand-mark"></span>Plorvan Pte Ltd</div>
  <div class="f-badge abs"></div>
  <p class="follow abs">Follow us:</p>
  <div class="socials abs"><span></span><span></span><span></span><span></span></div>

  <div class="f-col abs" style="left:453px;top:46px">
    <h3>Quick links</h3>
    <ul class="f-links"><li>About</li><li>Services</li><li>Gallery</li><li>Calculators</li><li>Blog</li><li>Contact</li></ul>
  </div>
  <div class="f-col abs" style="left:757px;top:46px;width:300px">
    <h3>Contact us</h3>
    <div class="f-info"><svg width="16" height="18" viewBox="0 0 16 18"><path d="M8 17s6-6 6-10A6 6 0 002 7c0 4 6 10 6 10z" fill="#FFC000"/><circle cx="8" cy="7" r="2" fill="#242424"/></svg><span>14 Orvale Lane #05-11/11A<br>Brenholt House Singapore 000214</span></div>
    <div class="f-info"><svg width="16" height="16" viewBox="0 0 16 16"><path d="M3 1l3 3-2 2c1 2 3 4 5 5l2-2 3 3-2 3C7 15 1 9 1 3z" fill="#FFC000"/></svg><span>+65 6000 1280</span></div>
    <div class="f-info"><svg width="16" height="18" viewBox="0 0 16 18"><rect x="3" y="1" width="10" height="16" rx="1.5" fill="none" stroke="#FFC000" stroke-width="2"/></svg><span>+65 9000 4617</span></div>
    <div class="f-info"><svg width="16" height="14" viewBox="0 0 16 14"><rect x="1" y="2" width="14" height="10" fill="#FFC000"/><path d="M1 2l7 5 7-5" fill="none" stroke="#242424" stroke-width="1.2"/></svg><span>hello@plorvan.example</span></div>
  </div>
  <div class="copy-line abs"></div>
  <p class="copy abs">Copyright 2023 © All rights reserved.</p>
</footer>

</body>
</html>
```